Business card (AI file uploaded)

We need a business card design that is minimalist using existing logo (attached). Source files must be editable so we can make the same design with other names.

Screenshots included of a design I was working on to give you an idea of the style I would like. Looking for similar modern styles

Thanks

```html
<!DOCTYPE html>
<html lang="en">
<head>
<meta charset="utf-8">
<title>Harlow Law Group – Business Card</title>
<link rel="stylesheet" href="https://fonts.googleapis.com/css2?family=Questrial&display=swap">
<style>
  :root {
    --stage-light: #ffffff;
    --stage-dark: #c9c9c9;
    --card-black: #000000;
    --card-white: #ffffff;
    --ink-white: #ffffff;
    --ink-black: #111111;
    --ink-muted: #9a9a9a;
    --rule-red: #c8401f;
  }
  * { margin: 0; padding: 0; box-sizing: border-box; }
  html, body { width: 1034px; height: 1200px; overflow: hidden; }
  body {
    position: relative;
    font-family: "Questrial", "Century Gothic", sans-serif;
    background: radial-gradient(ellipse 70% 60% at 50% 50%, var(--stage-light) 40%, var(--stage-dark) 100%);
  }
  .card {
    position: absolute;
    left: 160px;
    width: 691px;
    height: 404px;
  }
  .card--front { top: 135px; background: var(--card-black); color: var(--ink-white); }
  .card--back { top: 663px; height: 406px; background: var(--card-white); color: var(--ink-black); }

  .brand { position: absolute; display: flex; align-items: center; }
  .brand__mark { flex: none; }
  .brand__name { text-transform: uppercase; line-height: 1; margin-left: 14px; }
  .brand__primary { display: block; letter-spacing: 1px; }
  .brand__secondary { display: block; letter-spacing: 4px; }
  .brand__suffix { font-size: 0.3em; letter-spacing: 0; }

  .card--front .brand { left: 100px; top: 120px; }
  .card--front .brand__primary { font-size: 72px; }
  .card--front .brand__secondary { font-size: 37px; margin-top: 4px; }

  .card--back .brand { left: 165px; top: 72px; }
  .card--back .brand__primary { font-size: 62px; }
  .card--back .brand__secondary { font-size: 31px; margin-top: 3px; }

  .practice-areas {
    position: absolute;
    left: 0; right: 0; top: 357px;
    text-align: center;
    font-size: 19px;
    color: var(--ink-muted);
    letter-spacing: 0.3px;
  }
  .practice-areas .sep { margin: 0 6px; }

  .contact {
    position: absolute;
    left: 93px; width: 505px; top: 240px;
    text-align: center;
  }
  .contact__header {
    display: flex; align-items: baseline; justify-content: center;
    padding-bottom: 6px;
    border-bottom: 3px solid var(--rule-red);
  }
  .contact__name { font-size: 40px; letter-spacing: 2px; text-transform: uppercase; }
  .contact__title { font-size: 19px; margin-left: 24px; }
  .contact__details { font-size: 19px; line-height: 24px; margin-top: 4px; }
  .contact__details .gap { display: inline-block; width: 18px; }
</style>
</head>
<body>
  <section class="card card--front">
    <div class="brand">
      <svg class="brand__mark" width="112" height="112" viewBox="0 0 112 112" aria-hidden="true">
        <circle cx="56" cy="56" r="50" fill="none" stroke="var(--ink-white)" stroke-width="5"/>
      </svg>
      <div class="brand__name">
        <span class="brand__primary">Harlow</span>
        <span class="brand__secondary">Law Group <span class="brand__suffix">PC</span></span>
      </div>
    </div>
    <p class="practice-areas">Real Estate<span class="sep">|</span>Bankruptcy<span class="sep">|</span>Social Security Disability</p>
  </section>

  <section class="card card--back">
    <div class="brand">
      <svg class="brand__mark" width="100" height="100" viewBox="0 0 100 100" aria-hidden="true">
        <circle cx="50" cy="50" r="45" fill="none" stroke="var(--ink-black)" stroke-width="5"/>
      </svg>
      <div class="brand__name">
        <span class="brand__primary">Harlow</span>
        <span class="brand__secondary">Law Group <span class="brand__suffix">PC</span></span>
      </div>
    </div>
    <div class="contact">
      <div class="contact__header">
        <span class="contact__name">Daniel Harlow</span>
        <span class="contact__title">Attorney At Law</span>
      </div>
      <p class="contact__details">
        410 Meridian Ave., Suite 200, Westfield, IL 60599<br>
        P: 630.555.0148<span class="gap"></span>F: 630.555.0172<br>
        harlow@harlowlaw.com
      </p>
    </div>
  </section>
</body>
</html>
```